AK MERIDEL BUSINESS CARD DESIGN PROJECT

We need to utilize our logo that was expertly created on Markvelloo and now need to match this with a business card design.

```html
<!DOCTYPE html>
<html lang="en">
<head>
<meta charset="utf-8">
<title>AK MERIDEL Business Card</title>
<link href="https://fonts.googleapis.com/css2?family=Open+Sans:wght@400;600;700;800&display=swap" rel="stylesheet">
<style>
  :root {
    --stage: #232323;
    --brand-blue: #1658a7;
    --card-white: #ffffff;
    --ink: #1a1a1a;
  }
  * { margin: 0; padding: 0; box-sizing: border-box; }
  html, body {
    width: 1200px; height: 780px; overflow: hidden;
    background: var(--stage);
    font-family: "Open Sans", Arial, sans-serif;
  }
  .stage {
    position: relative; width: 1200px; height: 780px;
    display: flex; align-items: center; justify-content: center; gap: 40px;
  }
  .card {
    position: relative; width: 540px; height: 309px; overflow: hidden;
    box-shadow: 0 14px 30px rgba(0,0,0,0.55);
  }
  .card-front {
    background: var(--brand-blue);
    display: flex; align-items: center; justify-content: center;
  }
  .wordmark {
    font-weight: 800; letter-spacing: 4px; white-space: nowrap;
  }
  .card-front .wordmark { color: var(--card-white); font-size: 44px; }
  .card-back { background: var(--card-white); }
  .edge-band { position: absolute; width: 14px; background: var(--brand-blue); }
  .edge-band-left { left: 0; top: 118px; height: 172px; }
  .edge-band-right { right: 0; top: 42px; height: 108px; }
  .back-wordmark {
    position: absolute; left: 34px; top: 138px;
    color: var(--brand-blue); font-size: 26px; letter-spacing: 2px;
  }
  .divider {
    position: absolute; left: 248px; top: 70px; width: 1.5px; height: 162px;
    background: var(--ink);
  }
  .contact { position: absolute; left: 272px; top: 62px; color: var(--ink); }
  .contact-name {
    color: var(--brand-blue); font-weight: 700; font-size: 25px; line-height: 1.1;
  }
  .contact-role { font-weight: 600; font-size: 13px; margin: 3px 0 14px 14px; }
  .contact-list { list-style: none; margin-left: 22px; }
  .contact-list li {
    display: flex; align-items: center; gap: 7px;
    font-size: 13px; line-height: 18px;
  }
  .contact-list svg { width: 13px; height: 13px; flex: none; }
  .address {
    position: absolute; left: 262px; top: 262px;
    font-size: 13px; color: var(--ink);
  }
</style>
</head>
<body>
  <main class="stage">
    <section class="card card-front" aria-label="Business card front">
      <span class="wordmark">AK MERIDEL</span>
    </section>

    <section class="card card-back" aria-label="Business card back">
      <span class="edge-band edge-band-left"></span>
      <span class="edge-band edge-band-right"></span>
      <span class="wordmark back-wordmark">AK MERIDEL</span>
      <span class="divider"></span>
      <div class="contact">
        <h1 class="contact-name">Daniel T. Ruskin</h1>
        <p class="contact-role">Owner</p>
        <ul class="contact-list">
          <li>
            <svg viewBox="0 0 13 13" aria-hidden="true"><rect x="3" y="1" width="7" height="11" rx="1" fill="none" stroke="#1658a7" stroke-width="1.3"/></svg>
            555-210-3876
          </li>
          <li>
            <svg viewBox="0 0 13 13" aria-hidden="true"><circle cx="6.5" cy="6.5" r="5.5" fill="#1658a7"/><path d="M1 6.5h11M6.5 1c-2.5 3-2.5 8 0 11M6.5 1c2.5 3 2.5 8 0 11" stroke="#fff" stroke-width="0.8" fill="none"/></svg>
            www.akmeridel.com
          </li>
          <li>
            <svg viewBox="0 0 13 13" aria-hidden="true"><rect x="1" y="3" width="11" height="8" fill="#1658a7"/><path d="M1 3l5.5 4.5L12 3" stroke="#fff" stroke-width="1" fill="none"/></svg>
            danielruskin@akmeridel.com
          </li>
        </ul>
      </div>
      <p class="address">870 Larkfield Ave</p>
    </section>
  </main>
</body>
</html>
```